Small Business Consulting Firm Needs Business Card Design

Need a sleek modern business card with 2 sides matching the colors of our logo. We will be placing these with a mailer we are sending out. These business cards will only ever be given to business owners. We operate helping businesses who are struggling with cash flow or finances. If the green and blue design needs to be moved to the right of "Brightpath Ledger Consulting" for aesthetic purposes that is ok. We will need an editable file if possible. We would like to include the reps name, email, website, and phone number. For now just use Owen Parrish, oparrish@brightpathledger.com, www.brightpathledger.com, and 855-219-7038.

```html
<!DOCTYPE html>
<html lang="en">
<head>
<meta charset="UTF-8">
<title>Brightpath Ledger Consulting – Business Card</title>
<link rel="stylesheet" href="https://fonts.googleapis.com/css2?family=Lato:wght@300;400;700&display=swap">
<style>
  :root {
    --backdrop: #e4e4e4;
    --card-dark: #444444;
    --card-light: #ffffff;
    --brand-green: #6db33f;
    --brand-blue: #0a7cc1;
    --ink: #4a4a4a;
    --ink-soft: #6a6a6a;
    --on-dark: #f2f2f2;
  }
  * { box-sizing: border-box; margin: 0; padding: 0; }
  html, body {
    width: 1200px; height: 900px; overflow: hidden;
    background: var(--backdrop);
    font-family: "Lato", sans-serif;
  }
  .canvas {
    position: relative; width: 1200px; height: 900px;
  }
  .card {
    position: absolute;
    width: 560px; height: 320px;
    border-radius: 24px;
    box-shadow: 0 6px 18px rgba(0,0,0,0.18);
    overflow: hidden;
  }
  /* Back side */
  .card-back {
    left: 320px; top: 80px;
    background: var(--card-dark);
    display: flex; flex-direction: column; align-items: center; justify-content: center;
  }
  .brand-mark {
    width: 34px; height: 34px; background: var(--brand-green); margin-bottom: 22px;
  }
  .brand-name {
    color: var(--on-dark); font-weight: 300; font-size: 25px;
    letter-spacing: 3px; text-transform: uppercase;
  }
  .brand-sub {
    color: var(--on-dark); font-weight: 300; font-size: 11px;
    letter-spacing: 6px; text-transform: uppercase; margin-top: 4px;
  }
  /* Front side */
  .card-front {
    left: 320px; top: 480px;
    background: var(--card-light);
  }
  .front-brand {
    position: absolute; left: 40px; top: 110px;
  }
  .front-brand .brand-name { color: var(--ink); font-size: 24px; }
  .front-brand .brand-sub { color: var(--ink-soft); font-size: 10px; margin-left: 72px; }
  .rep {
    position: absolute; left: 40px; top: 196px;
  }
  .rep-name {
    font-weight: 700; font-size: 21px; letter-spacing: 1px; text-transform: uppercase;
    margin-bottom: 10px;
  }
  .rep-first { color: var(--brand-green); }
  .rep-last { color: var(--brand-blue); }
  .contact-list { list-style: none; }
  .contact-item {
    display: flex; align-items: center; gap: 9px;
    color: var(--ink-soft); font-size: 15px; line-height: 22px;
  }
  .contact-icon { width: 13px; height: 13px; flex: none; }
</style>
</head>
<body>
<main class="canvas">
  <section class="card card-back" aria-label="Card back">
    <div class="brand-mark"></div>
    <div class="brand-name">Brightpath Ledger</div>
    <div class="brand-sub">Consulting</div>
  </section>

  <section class="card card-front" aria-label="Card front">
    <div class="front-brand">
      <div class="brand-name">Brightpath Ledger</div>
      <div class="brand-sub">Consulting</div>
    </div>
    <div class="rep">
      <div class="rep-name"><span class="rep-first">Owen</span> <span class="rep-last">Parrish</span></div>
      <ul class="contact-list">
        <li class="contact-item">
          <svg class="contact-icon" viewBox="0 0 16 16" aria-hidden="true"><path fill="#6db33f" d="M3 1h3l1.5 4-2 1.2a9 9 0 0 0 4.3 4.3L11 8.5l4 1.5v3a2 2 0 0 1-2 2A12 12 0 0 1 1 3a2 2 0 0 1 2-2z"/></svg>
          855-219-7038
        </li>
        <li class="contact-item">
          <svg class="contact-icon" viewBox="0 0 16 16" aria-hidden="true"><rect x="1" y="3" width="14" height="10" rx="1" fill="#6db33f"/><path d="M1.5 3.5 8 9l6.5-5.5" stroke="#fff" stroke-width="1.4" fill="none"/></svg>
          oparrish@brightpathledger.com
        </li>
        <li class="contact-item">
          <svg class="contact-icon" viewBox="0 0 16 16" aria-hidden="true"><circle cx="8" cy="8" r="7" fill="#6db33f"/><path d="M1 8h14M8 1c-3 3.5-3 10.5 0 14M8 1c3 3.5 3 10.5 0 14" stroke="#fff" stroke-width="1.1" fill="none"/></svg>
          www.brightpathledger.com
        </li>
      </ul>
    </div>
  </section>
</main>
</body>
</html>
```